FOLI PACK FOR STICKS

Design the packaging for salted sticks (weight 400g) reference to the logo VOLK (in attached).
Color packaging- look forward to suggestions.
Package with window.
Hi, we need only graphic conception without texts on back side.

Please find Logo VOLK and the grid of packaging - attached
Updates

Target Market(s)

typical salted snack for everyone (adults and children included)

Font styles to use
Sans Serif

Requirements
Should not have
• - religion and politic signs…
• - toys and childdraws
• - monsters, devils and demons etc.

```html
<!DOCTYPE html>
<html lang="en">
<head>
<meta charset="utf-8">
<title>VOLK Salt Sticks – Front Panel</title>
<link rel="stylesheet" href="https://fonts.googleapis.com/css2?family=Roboto:wght@900&display=swap">
<style>
  :root {
    --bg: #ffffff;
    --stripe-light: #c5dba9;
    --stripe-dark: #b6ce99;
    --top-band: #a9c290;
    --olive: #4f5e27;
    --brand-brown: #6e4119;
    --band-white: #ffffff;
    --stick-light: #e9a055;
    --stick-dark: #b8641f;
    --wheat: #55652a;
    --salt: #e3e6e6;
    --label-white: #ffffff;
  }
  html, body {
    margin: 0;
    padding: 0;
    width: 1200px;
    height: 1000px;
    overflow: hidden;
    background: var(--bg);
  }
  .canvas {
    position: relative;
    width: 1200px;
    height: 1000px;
    background: var(--bg);
  }
  .pack {
    position: absolute;
    left: 388px;
    top: 150px;
    width: 434px;
    height: 575px;
  }
  .pack__art {
    display: block;
  }
  .brand-name,
  .weight-label,
  .flavour-small,
  .flavour-large {
    font-family: "Roboto", "Arial", sans-serif;
    font-weight: 900;
  }
  .brand-name {
    font-size: 52px;
    fill: var(--brand-brown);
  }
  .weight-label {
    font-size: 21px;
    fill: var(--label-white);
  }
  .flavour-small {
    font-size: 15px;
    fill: var(--olive);
  }
  .flavour-large {
    font-size: 38px;
    fill: var(--olive);
  }
</style>
</head>
<body>
<main class="canvas">
  <section class="pack" aria-label="VOLK salt sticks pack front">
    <svg class="pack__art" width="434" height="575" viewBox="0 0 434 575" xmlns="http://www.w3.org/2000/svg">
      <defs>
        <pattern id="stripes" width="24" height="10" patternUnits="userSpaceOnUse">
          <rect width="12" height="10" fill="var(--stripe-light)"/>
          <rect x="12" width="12" height="10" fill="var(--stripe-dark)"/>
        </pattern>
        <linearGradient id="sticks-tone" x1="0" y1="0" x2="1" y2="0">
          <stop offset="0" stop-color="var(--stick-dark)"/>
          <stop offset="0.5" stop-color="var(--stick-light)"/>
          <stop offset="1" stop-color="var(--stick-dark)"/>
        </linearGradient>
        <clipPath id="pack-shape">
          <path d="M0 10 L6 0 L12 10 L18 0 L24 10 L30 0 L36 10 L42 0 L48 10 L54 0 L60 10 L66 0 L72 10 L78 0 L84 10 L90 0 L96 10 L102 0 L108 10 L114 0 L120 10 L126 0 L132 10 L138 0 L144 10 L150 0 L156 10 L162 0 L168 10 L174 0 L180 10 L186 0 L192 10 L198 0 L204 10 L210 0 L216 10 L222 0 L228 10 L234 0 L240 10 L246 0 L252 10 L258 0 L264 10 L270 0 L276 10 L282 0 L288 10 L294 0 L300 10 L306 0 L312 10 L318 0 L324 10 L330 0 L336 10 L342 0 L348 10 L354 0 L360 10 L366 0 L372 10 L378 0 L384 10 L390 0 L396 10 L402 0 L408 10 L414 0 L420 10 L426 0 L434 10 L434 575 L0 575 Z"/>
        </clipPath>
      </defs>

      <g class="pack-body" clip-path="url(#pack-shape)">
        <rect class="stripes" width="434" height="575" fill="url(#stripes)"/>

        <!-- top seal band -->
        <path class="seal-band" fill="var(--top-band)"
          d="M0 0 L434 0 L434 62 C380 58 330 52 280 50 C220 48 170 62 120 64 C70 66 30 58 0 68 Z"/>

        <!-- wheat ears area -->
        <rect role="img" aria-label="Three wheat ears rising above the brand band"
          x="174" y="80" width="80" height="96" rx="28" fill="var(--wheat)" opacity="0.9"/>

        <!-- brand band -->
        <rect class="band-line" x="0" y="212" width="434" height="6" fill="var(--olive)"/>
        <rect class="band" x="0" y="218" width="434" height="104" fill="var(--band-white)"/>
        <rect class="band-line" x="0" y="322" width="434" height="6" fill="var(--olive)"/>
        <text class="brand-name" x="217" y="297" text-anchor="middle">VOLK</text>

        <!-- product window -->
        <path class="window-halo" fill="var(--stripe-light)" opacity="0.7"
          d="M50 328 A167 150 0 0 0 384 328 Z"/>
        <path class="window-rim" fill="var(--olive)"
          d="M62 328 A155 136 0 0 0 372 328 Z"/>
        <path role="img" aria-label="Window showing the salted sticks inside"
          fill="url(#sticks-tone)"
          d="M70 328 A147 128 0 0 0 364 328 Z"/>

        <!-- weight tag -->
        <g class="weight-tag" transform="translate(340 428) rotate(-45)">
          <rect x="-48" y="-19" width="96" height="38" rx="10" fill="var(--olive)"/>
          <text class="weight-label" x="0" y="8" text-anchor="middle">400g ℮</text>
        </g>

        <!-- salt pile area -->
        <rect role="img" aria-label="Pile of white salt crystals"
          x="98" y="482" width="74" height="64" rx="8" fill="var(--salt)"/>

        <!-- flavour name -->
        <text class="flavour-small" x="174" y="500">SALT</text>
        <text class="flavour-large" x="173" y="540">STICKS</text>

        <!-- bottom edge -->
        <rect class="bottom-line" x="0" y="565" width="434" height="8" fill="var(--olive)"/>
      </g>
    </svg>
  </section>
</main>
</body>
</html>
```